M Website

We need a website design for a construction plant company. You may use a combination of our photos and the stock images. See the logo for company colours. It also be of great value to see moving pictures like the ones on the link: https://www.quindellworks.co.za/copy-of-about-us. See our uploaded files for content.

Target Market(s)

Construction

Number of Pages Required

5+ page

```html
<!DOCTYPE html>
<html lang="en">
<head>
<meta charset="utf-8">
<title>K4 Haulage and Plant Hire — About</title>
<link href="https://fonts.googleapis.com/css2?family=Roboto+Condensed:wght@400;700;900&family=Roboto:wght@400;500&display=swap" rel="stylesheet">
<style>
  :root {
    --amber: #ecaf00;
    --ink: #222222;
    --body-text: #333333;
    --white: #ffffff;
    --dark-band: #1f1f1f;
    --sky-top: #6b86c4;
    --sky-low: #c9d3e2;
    --sand: #a9875c;
    --sand-dark: #7e6142;
  }
  * { margin: 0; padding: 0; box-sizing: border-box; }
  html, body { width: 849px; height: 1200px; overflow: hidden; background: var(--white); }
  body { position: relative; font-family: "Roboto", sans-serif; color: var(--body-text); }

  .hero { position: absolute; left: 0; top: 0; width: 849px; height: 569px; overflow: hidden; }
  .hero-photo {
    position: absolute; inset: 0;
    background: linear-gradient(180deg, var(--sky-top) 0%, #9fb1d6 30%, var(--sky-low) 55%, #b89a70 75%, var(--sand) 88%, var(--sand-dark) 100%);
  }

  .brand { position: absolute; left: 29px; top: 20px; display: flex; align-items: center; gap: 6px; }
  .brand-dot { width: 14px; height: 14px; border-radius: 50%; background: var(--amber); }
  .brand-name { font-family: "Roboto Condensed", sans-serif; font-weight: 700; font-size: 22px; color: var(--amber); }

  .main-nav { position: absolute; top: 28px; left: 0; width: 849px; }
  .nav-item {
    position: absolute; font-family: "Roboto", sans-serif; font-size: 9px; letter-spacing: 2px;
    color: #2c3550; text-transform: uppercase;
  }
  .nav-item.active { color: var(--ink); font-weight: 500; }
  .nav-item.active::before { content: "["; color: var(--amber); margin-right: 6px; }
  .nav-item.active::after { content: "]"; color: var(--amber); margin-left: 4px; }

  .hero-mark {
    position: absolute; left: 26px; top: 118px;
    font-family: "Roboto Condensed", sans-serif; font-weight: 900; font-size: 280px; line-height: 1;
    color: var(--amber); letter-spacing: 4px;
  }
  .hero-title {
    position: absolute; right: 18px; top: 176px; text-align: right;
    font-family: "Roboto Condensed", sans-serif; font-weight: 700; font-size: 33px; line-height: 40px;
    color: var(--white); text-transform: uppercase;
  }
  .hero-tagline {
    position: absolute; right: 13px; top: 281px;
    font-family: "Roboto", sans-serif; font-weight: 500; font-size: 10px; letter-spacing: 2.6px;
    color: var(--white); text-transform: uppercase;
  }
  .corner { position: absolute; }

  .texture { position: absolute; background: linear-gradient(135deg, #f6f6f6 0%, rgba(255,255,255,0) 100%); }

  .section-title {
    position: absolute; left: 0; width: 849px; top: 616px; text-align: center;
    font-family: "Roboto Condensed", sans-serif; font-weight: 700; font-size: 22px; color: var(--ink);
  }

  .mission-photo {
    position: absolute; left: 370px; top: 726px; width: 479px; height: 352px;
    background: linear-gradient(180deg, #c9d6dd 0%, #a3a08f 35%, #7a6b55 70%, #8c7760 100%);
  }
  .mission-card {
    position: absolute; left: 32px; top: 758px; width: 432px; height: 234px;
    background: var(--white); box-shadow: 0 4px 18px rgba(0,0,0,0.14);
    padding: 28px 36px 0 36px;
  }
  .mission-card p { font-size: 13px; line-height: 24.8px; color: var(--body-text); }

  .promise-band {
    position: absolute; left: 461px; top: 1040px; width: 388px; height: 89px;
    background: var(--dark-band); color: var(--white);
    font-family: "Roboto", sans-serif; font-weight: 500; font-size: 10.5px; letter-spacing: 2.5px;
    text-transform: uppercase; line-height: 24px; padding-top: 18px;
  }
  .promise-band .line { display: block; padding-left: 32px; }
  .promise-band .bracket { color: var(--amber); }
</style>
</head>
<body>

<header class="hero">
  <div class="hero-photo" role="img" aria-label="Photo of a yellow excavator on a large sand mound beside a highway overpass under a cloudy blue sky"></div>

  <div class="brand">
    <span class="brand-dot"></span>
    <span class="brand-name">K4</span>
  </div>

  <nav class="main-nav">
    <span class="nav-item active" style="left:490px">About</span>
    <span class="nav-item" style="left:582px">Projects</span>
    <span class="nav-item" style="left:691px">News</span>
    <span class="nav-item" style="left:780px">Contacts</span>
  </nav>

  <div class="hero-mark">K4</div>

  <svg class="corner" style="left:567px;top:174px" width="14" height="14"><path d="M1 14V1H14" fill="none" stroke="#ecaf00" stroke-width="3"/></svg>
  <h1 class="hero-title">K4 Haulage and<br>Plant Hire</h1>
  <svg class="corner" style="left:830px;top:249px" width="14" height="14"><path d="M0 13H13V0" fill="none" stroke="#ecaf00" stroke-width="3"/></svg>
  <p class="hero-tagline">Transformig our clients vision into reality</p>
</header>

<div class="texture" style="left:0;top:572px;width:240px;height:420px" role="img" aria-label="Faint grid of small plus marks"></div>
<div class="texture" style="left:612px;top:1132px;width:220px;height:68px" role="img" aria-label="Faint grid of small plus marks"></div>

<svg class="corner" style="left:380px;top:613px" width="10" height="10"><path d="M1 10V1H10" fill="none" stroke="#ecaf00" stroke-width="2"/></svg>
<h2 class="section-title">MISSION</h2>
<svg class="corner" style="left:463px;top:636px" width="10" height="10"><path d="M0 9H9V0" fill="none" stroke="#ecaf00" stroke-width="2"/></svg>

<div class="mission-photo" role="img" aria-label="Photo of two men shaking hands in front of yellow backhoe loaders on a low-bed truck"></div>

<svg class="corner" style="left:18px;top:745px" width="28" height="28"><path d="M2 28V2H28" fill="none" stroke="#ecaf00" stroke-width="4"/></svg>
<article class="mission-card">
  <p>K4 Haulage and Plant Hire (Pty) Ltd aims to employ the professional skills of it’s well accomplished staff in providing efficient and sustainable engineering construction solutions to our Clients for the benefit of various stakeholders and community at large. As such, we aim to transform both Public and Private sector visions into realities.</p>
</article>
<svg class="corner" style="left:450px;top:978px" width="28" height="28"><path d="M0 26H26V0" fill="none" stroke="#ecaf00" stroke-width="4"/></svg>

<aside class="promise-band">
  <span class="line"><span class="bracket">[</span>&nbsp; Delivering high quality multidisciplinary</span>
  <span class="line">&nbsp;&nbsp;Engineering and construction projects &nbsp;<span class="bracket">]</span></span>
</aside>

</body>
</html>
```